Book Cover Design Book About Commercial Real Estate Investing

I need a book cover designed for my upcoming book.
Need cover for paperback and hardcover book.

The Book is about investing in net lease commercial property.

The book title:

The Ground Rent Handbook
Proven Methods For KVR Asset Buyers
By Lou Barrow

Should be minimalist, clean, authoritative, convey money, trust, & growth
I think I like the colors white red and black.
I want a front cover at this time.

Samples I like are included. - the red white and blacks are my favorites

My company is The KVR Circle
you can learn more about Triple Net Properties at my website
www.TheKVRCircle.com

the symbol NNN = Triple net in commercial real estate

Target Market(s)

Affluent male conservative investors

Industry/Entity Type

Real Estate

Requirements
Nice to have
• Sports Motif - - diagrams of sports plays from playbook
• google - Diagrams of sports plays -

```html
<!DOCTYPE html>
<html lang="en">
<head>
<meta charset="utf-8">
<title>The Ground Rent Handbook — Front Cover</title>
<link rel="stylesheet" href="https://fonts.googleapis.com/css2?family=Saira+Condensed:wght@500;600&family=Playfair+Display:wght@900&family=Tinos&family=Arimo&display=swap">
<style>
  :root {
    --cover-blue: #2161ac;
    --spine-blue: #2a66b0;
    --frame-cyan: #1d9ad8;
    --inner-rule: #6fa9dd;
    --band-red: #c0222a;
    --ink-white: #ffffff;
  }
  html, body {
    margin: 0;
    padding: 0;
    overflow: hidden;
  }
  .cover {
    position: relative;
    width: 1079px;
    height: 1200px;
    background: var(--cover-blue);
    overflow: hidden;
    color: var(--ink-white);
  }
  .spine {
    position: absolute;
    left: 0;
    top: 0;
    width: 146px;
    height: 1200px;
    background: var(--spine-blue);
    border-right: 2px solid #3c78bf;
  }
  .spine svg { display: block; }
  .spine-title {
    font-family: "Saira Condensed", sans-serif;
    font-weight: 500;
    fill: var(--ink-white);
  }
  .front-frame {
    position: absolute;
    left: 181px;
    top: 63px;
    width: 842px;
    height: 1072px;
    border: 12px solid var(--frame-cyan);
  }
  .front-rule {
    position: absolute;
    left: 202px;
    top: 85px;
    width: 822px;
    height: 1051px;
    border: 2px solid var(--inner-rule);
  }
  .title-line {
    position: absolute;
    left: 196px;
    width: 834px;
    margin: 0;
    text-align: center;
    font-family: "Saira Condensed", sans-serif;
    font-weight: 500;
    letter-spacing: 5px;
    line-height: 1;
  }
  .title-top {
    top: 192px;
    font-size: 112px;
  }
  .title-band {
    top: 309px;
    height: 141px;
    background: var(--band-red);
    font-size: 132px;
    line-height: 141px;
  }
  .subtitle {
    position: absolute;
    left: 196px;
    width: 834px;
    top: 640px;
    margin: 0;
    text-align: center;
    font-family: "Saira Condensed", sans-serif;
    font-weight: 600;
    font-size: 48px;
    letter-spacing: 2.5px;
    line-height: 64px;
  }
  .author {
    position: absolute;
    left: 196px;
    width: 834px;
    top: 806px;
    margin: 0;
    text-align: center;
    font-family: "Playfair Display", serif;
    font-weight: 900;
    font-size: 74px;
    line-height: 1;
    transform: scaleX(0.86);
  }
  .edition-year {
    position: absolute;
    left: 196px;
    width: 834px;
    top: 918px;
    margin: 0;
    text-align: center;
    font-family: "Tinos", serif;
    font-size: 66px;
    line-height: 1;
  }
  .website {
    position: absolute;
    right: 71px;
    top: 1104px;
    margin: 0;
    font-family: "Arimo", sans-serif;
    font-size: 22px;
    line-height: 1;
  }
</style>
</head>
<body>
  <main class="cover">
    <aside class="spine">
      <svg width="146" height="1200" viewBox="0 0 146 1200" aria-label="The Ground Rent Handbook">
        <text class="spine-title" transform="translate(128 1125) rotate(-90)" textLength="1010" lengthAdjust="spacingAndGlyphs">
          <tspan font-size="66">THE GROUND RENT</tspan><tspan font-size="80">HANDBOOK</tspan>
        </text>
      </svg>
    </aside>

    <div class="front-frame"></div>
    <div class="front-rule"></div>

    <h1 class="title-line title-top">THE GROUND RENT</h1>
    <p class="title-line title-band">HANDBOOK</p>

    <p class="subtitle">Proven Methods For KVR<br>Asset Buyers</p>
    <p class="author">By Lou Barrow</p>
    <p class="edition-year">2002</p>
    <p class="website">www.TheKVRCircle.com</p>
  </main>
</body>
</html>
```